Brennick - Business Card Design

Design a modern masculine business card for our business

Target Market(s)

Private Market

Industry/Entity Type

Construction

Contact Information for Business Card

Company Name - Name of Person - Address - email address - contact number

Font styles to use
Serif
Sans Serif

Colors
0094D4
00A9DD
6FCCEA
C7EBF8
E9F6FB
00AB8E
00BBA5
67D7C9
C6EFE9
E9F9F6
F0912C
F2A743
F7CA91
FBE8D2
FDF5EE

Requirements
Must have
• Use company logo provided
Nice to have
• Company Logo

```html
<!DOCTYPE html>
<html lang="en">
<head>
<meta charset="utf-8">
<title>Brennick – Business Card</title>
<link href="https://fonts.googleapis.com/css2?family=Montserrat:wght@500;800&family=Orbitron:wght@800&display=swap" rel="stylesheet">
<style>
  :root {
    --stage: #1c1c1e;
    --ink: #0b0b0b;
    --paper: #ffffff;
    --accent: #f26a22;
    --text-dark: #111111;
  }
  * { margin: 0; padding: 0; box-sizing: border-box; }
  html, body { width: 1200px; height: 886px; overflow: hidden; background: var(--stage); }
  .canvas { position: relative; width: 1200px; height: 886px; }

  .card {
    position: absolute;
    width: 560px; height: 320px;
    border-radius: 28px;
    overflow: hidden;
    box-shadow: 0 18px 40px rgba(0,0,0,.55);
  }

  /* Back side */
  .card-back { left: 110px; top: 90px; background: var(--ink); }
  .card-back .brand {
    position: absolute; inset: 0;
    display: flex; align-items: center; justify-content: center; gap: 16px;
  }
  .brand-mark { width: 22px; height: 22px; background: var(--accent); flex: none; }
  .card-back .brand-name {
    font-family: "Montserrat", sans-serif; font-weight: 800;
    font-size: 66px; letter-spacing: 2px; color: var(--paper);
    white-space: nowrap;
  }

  /* Front side */
  .card-front { left: 530px; top: 480px; background: var(--paper); }
  .front-bands { position: absolute; inset: 0; }
  .card-front .brand {
    position: absolute; left: 36px; top: 56px;
    display: flex; align-items: center; gap: 10px;
  }
  .card-front .brand-mark { width: 12px; height: 12px; }
  .card-front .brand-name {
    font-family: "Montserrat", sans-serif; font-weight: 800;
    font-size: 30px; letter-spacing: 1px; color: var(--text-dark);
    white-space: nowrap;
  }
  .person-name {
    position: absolute; left: 38px; top: 150px;
    font-family: "Orbitron", sans-serif; font-weight: 800; font-size: 24px;
    color: var(--text-dark); letter-spacing: 1px; white-space: nowrap;
  }
  .contact-list {
    position: absolute; left: 296px; top: 44px;
    list-style: none;
    font-family: "Montserrat", sans-serif; font-weight: 500;
    font-size: 15px; color: var(--text-dark);
  }
  .contact-list li { display: flex; align-items: center; gap: 10px; height: 28px; white-space: nowrap; }
  .contact-list svg { width: 16px; height: 16px; flex: none; }
</style>
</head>
<body>
<main class="canvas">

  <section class="card card-back" aria-label="Business card back">
    <div class="brand">
      <span class="brand-mark"></span>
      <span class="brand-name">BRENNICK</span>
    </div>
  </section>

  <section class="card card-front" aria-label="Business card front">
    <svg class="front-bands" viewBox="0 0 560 320" preserveAspectRatio="none" aria-hidden="true">
      <polygon points="0,320 0,282 400,220 560,190 560,320" fill="var(--accent)"/>
      <polygon points="430,214 560,138 560,196 460,228" fill="var(--ink)"/>
      <polygon points="410,218 430,214 460,228 440,232" fill="var(--paper)"/>
    </svg>

    <div class="brand">
      <span class="brand-name">BRENNICK</span>
      <span class="brand-mark"></span>
    </div>

    <div class="person-name">MARK DALTON</div>

    <ul class="contact-list">
      <li>
        <svg viewBox="0 0 16 16"><path d="M8 1a5 5 0 0 0-5 5c0 4 5 9 5 9s5-5 5-9a5 5 0 0 0-5-5zm0 7a2 2 0 1 1 0-4 2 2 0 0 1 0 4z" fill="var(--accent)"/></svg>
        0456 Ridge Ave. Denver
      </li>
      <li>
        <svg viewBox="0 0 16 16" fill="none" stroke="var(--accent)" stroke-width="1.4"><circle cx="8" cy="8" r="6.5"/><ellipse cx="8" cy="8" rx="3" ry="6.5"/><path d="M1.5 8h13M2.5 4.8h11M2.5 11.2h11"/></svg>
        info@brennickbuild.com
      </li>
      <li>
        <svg viewBox="0 0 16 16"><path d="M3.5 1.5l2.5 0 1 3.5-1.6 1.2a8 8 0 0 0 4.4 4.4L11 9l3.5 1v2.5c0 1-1 2-2 2A11 11 0 0 1 1.5 3.5c0-1 1-2 2-2z" fill="var(--accent)"/></svg>
        555.204.7781
      </li>
    </ul>
  </section>

</main>
</body>
</html>
```